Howard Lindqvist and Dennis Ashworth Advertisement

We would like an ad that conveys understated elegance. We are a company that purchases estate jewelry watches and diamonds. We care to a wealthy, upscale clientele.

Target Market(s)

Wealthy upscale.

Industry/Entity Type

It Company

Requirements
Must have
• Elegant Design. Crisp Clean. Attached a doc of how the ad should be arranged.

```html
<!DOCTYPE html>
<html lang="en">
<head>
<meta charset="utf-8">
<title>Howard Lindqvist &amp; Dennis Ashworth — Ready To Sell?</title>
<link rel="stylesheet" href="https://fonts.googleapis.com/css2?family=Playfair+Display:wght@700;800&family=Crimson+Pro:wght@600&display=swap">
<style>
  :root {
    --page-bg: #e4e4e4;
    --frame: #ffffff;
    --ink: #141414;
    --glow-center: #ffffff;
    --glow-mid: #f1f1f1;
    --glow-edge: #c4c4c4;
    --stone-light: #fbfbfb;
    --stone-mid: #d2d2d2;
    --stone-dark: #8f8f8f;
  }
  * { margin: 0; padding: 0; box-sizing: border-box; }
  html, body {
    width: 1200px;
    height: 1200px;
    overflow: hidden;
    background: var(--page-bg);
  }
  .canvas {
    position: relative;
    width: 1200px;
    height: 1200px;
  }
  .ad {
    position: absolute;
    left: 150px;
    top: 16px;
    width: 900px;
    height: 1168px;
    background: var(--frame);
    padding: 13px;
  }
  .ad-surface {
    position: relative;
    width: 100%;
    height: 100%;
    overflow: hidden;
    background:
      radial-gradient(ellipse 70% 55% at 50% 48%, var(--glow-center) 0%, var(--glow-mid) 45%, var(--glow-edge) 100%);
    text-align: center;
    color: var(--ink);
  }
  .headline {
    position: absolute;
    left: 0; right: 0;
    top: 80px;
    font-family: "Playfair Display", serif;
    font-weight: 800;
    font-size: 78px;
    letter-spacing: -2px;
    line-height: 1;
  }
  .stone {
    position: absolute;
    left: 264px;
    top: 236px;
    width: 345px;
    height: 322px;
    border-radius: 34px;
    transform: rotate(-9deg);
    background: linear-gradient(145deg, var(--stone-light) 0%, var(--stone-mid) 45%, var(--stone-light) 62%, var(--stone-dark) 100%);
    box-shadow: 0 26px 30px -18px rgba(0,0,0,0.35);
  }
  .brand-name {
    position: absolute;
    left: 0; right: 0;
    top: 690px;
    font-family: "Crimson Pro", serif;
    font-weight: 600;
    font-size: 23px;
    line-height: 1;
    color: var(--ink);
  }
  .promise {
    position: absolute;
    left: 0; right: 0;
    top: 778px;
    font-family: "Playfair Display", serif;
    font-weight: 700;
    font-size: 44px;
    letter-spacing: 1.5px;
    line-height: 60px;
  }
  .contact {
    position: absolute;
    left: 0; right: 0;
    top: 946px;
    font-family: "Crimson Pro", serif;
    font-weight: 600;
    font-size: 23px;
    line-height: 31px;
    font-style: normal;
  }
</style>
</head>
<body>
<main class="canvas">
  <article class="ad">
    <div class="ad-surface">
      <h1 class="headline">Ready To Sell?</h1>
      <div class="stone" role="img" aria-label="Photograph of a large emerald-cut diamond"></div>
      <p class="brand-name">Howard Lindqvist &amp; Dennis Ashworth</p>
      <p class="promise">Utmost Discretion<br>By Appointment</p>
      <address class="contact">
        Via Serena<br>
        318-B Coral Avenue<br>
        Palm Beach, FL 33480<br>
        support@halindash.com<br>
        561.555.0142
      </address>
    </div>
  </article>
</main>
</body>
</html>
```